Flyer für Photovoltaikanlagen
Zielgruppe
Aufbau bzw. unterteilung, stelle ich mir vor das es wie auf 0124_pv_aquise_a4_lws.pdf ausgelegt.
FesterBestandteile:
- Abreißkarte wie auf Flyer 1:1
- Produktfotos + Logo ( Modul KE-Lumin, QVR Batterie, Helvorn - Wechselrichter ) am besten über die Abreißkarte
- Schönes Fotos mit Dachanlage ( wenn möglich dunkele Module / Full Black Module)
- Rechnen Bsp. zur Unabhängigkeit, wie auf dem anghängten Angebot.( Seite 2 )
Inhalte die eingbaut werden sollten, wenn möglich:
Wir bauen Photovoltaikanlagen und sind Dachdeckermeisterbetrieben und Elektromeisterbetrieb (evtl. auch als Logos)
Photovoltaikanlagen Neubau / Erweiterung
- Bedarfgerechte Beratung inkl. Besichtung der Immobilie
- Transparentes Angebot
- Netzanfrage
- Markstammdatenregisterung (Vergütung für verkaufen Strom)
- Planung & Auslegung (internes Ingeneurbüro)
- Montage Dach(Dachdeckermeisterbetrieb)
- Monate Elektro inkl. Zähersetzung (Elektromeisterbetrieb)
- Einweisung ins Monitoring (App)
After Sales Service
- Service & Wartung
- Reinigung
Modern
Bedarfweckend
Produktfotos verwenden

```html
<!DOCTYPE html>
<html lang="de">
<head>
<meta charset="utf-8">
<title>Flyer Photovoltaikanlagen</title>
<link href="https://fonts.googleapis.com/css2?family=Bebas+Neue&family=Poppins:wght@400;600;700;800&display=swap" rel="stylesheet">
<style>
:root{
  --blue:#3d5675;
  --blue-dark:#33496a;
  --yellow:#f4c955;
  --row:#e6e7e8;
  --white:#ffffff;
  --stage:#b8b8b8;
  --text:#3e4a5c;
}
*{margin:0;padding:0;box-sizing:border-box}
html,body{width:1200px;height:1117px;overflow:hidden;background:var(--stage)}
body{position:relative;font-family:'Poppins',sans-serif;color:var(--blue-dark)}
.page{position:absolute;top:174px;width:544px;height:769px;background:var(--white);overflow:hidden;box-shadow:0 3px 8px rgba(0,0,0,.25)}
.page--front{left:46px}
.page--back{left:609px}
.layer{position:absolute;left:0;top:0;width:544px;height:769px}
.photo{position:absolute}
.headline{font-family:'Bebas Neue',sans-serif;font-weight:400;line-height:1;white-space:nowrap}
.brand{position:absolute;display:flex;align-items:center;gap:6px;font-weight:800;font-size:13px;letter-spacing:.5px;line-height:1.1}
.brand__dot{width:14px;height:14px;border-radius:50%;background:var(--yellow);flex:none}

/* front */
.front-photo{left:0;top:0;width:544px;height:300px;background:linear-gradient(180deg,#c9d8e6 0%,#a9bdd2 35%,#7189a5 70%,rgba(61,86,117,0) 100%)}
.front-brand{left:215px;top:70px;color:var(--blue-dark);width:120px}
.front-title{position:absolute;left:40px;top:196px;color:var(--white);font-size:52px}
.front-sub{position:absolute;left:40px;top:243px;color:var(--yellow);font-size:33px}
.front-intro{position:absolute;left:40px;top:287px;width:258px;color:var(--white);font-size:9.3px;font-weight:600;line-height:12.1px}
.module-photo{left:310px;top:289px;width:234px;height:430px;background:linear-gradient(90deg,#2c2c2e,#3a3a3c 50%,#2a2a2c);border-left:2px solid #555;border-top:2px solid #555}
.spec-title{position:absolute;left:40px;top:430px;font-size:38px;color:var(--blue-dark)}
.spec{position:absolute;left:28px;top:472px;width:264px;border-collapse:separate;border-spacing:2px 0;font-size:9px;font-weight:600}
.spec td{height:26px;padding-left:10px;color:var(--text)}
.spec td:first-child{width:110px}
.spec tr:nth-child(odd) td{background:var(--row)}
.spec td:last-child{padding-left:14px}
.cta{position:absolute;left:40px;top:711px;font-size:20.5px;font-weight:800;line-height:21px;color:var(--blue-dark)}
.cta-phone{position:absolute;left:216px;top:729px;font-size:16.5px;font-weight:800;color:var(--blue-dark);display:flex;align-items:center;gap:4px}
.cta-phone span{font-weight:700;margin-right:6px}

/* back */
.back-photo{left:0;top:0;width:544px;height:340px;background:linear-gradient(135deg,#c98a52 0%,#5d6b84 35%,#3a4a66 65%,#263654 100%)}
.back-brand{left:40px;top:70px;color:var(--white);width:120px}
.services{position:absolute;left:311px;top:35px;width:233px;height:270px;background:var(--yellow);border-top-left-radius:14px;list-style:none;padding:10px 0 0 12px}
.services li{display:flex;gap:10px;font-size:8.8px;font-weight:700;line-height:10.4px;color:var(--blue-dark);margin-bottom:10.5px}
.services svg{flex:none;margin-top:1px}
.claim{position:absolute;left:40px;top:151px;width:271px;height:178px;background:var(--blue);padding:16px 0 0 24px;color:var(--white);font-size:39.5px;line-height:36px}
.claim em{font-style:normal;color:var(--yellow)}
.why{position:absolute;left:38px;top:352px;font-size:25px;color:var(--blue-dark)}
.col-left{position:absolute;left:40px;top:385px;width:258px}
.col-left h3{font-size:10.6px;font-weight:700;line-height:13px;color:var(--blue-dark);margin-bottom:9px}
.col-left p{font-size:8.6px;line-height:10.4px;color:var(--text);margin-bottom:10px}
.divider{position:absolute;left:308px;top:388px;width:1px;height:305px;background:#b9c0ca}
.col-right{position:absolute;left:322px;top:383px;width:200px}
.col-right h3{font-size:10.6px;font-weight:700;line-height:13px;color:var(--blue-dark);margin-bottom:9px;padding-left:9px}
.col-right h3 u{text-decoration:none;border-bottom:2px solid var(--yellow)}
.step{display:flex;gap:8px;margin-bottom:10px}
.step h4{font-size:11.2px;font-weight:700;color:var(--blue-dark);line-height:13px;margin-bottom:2px}
.step p{font-size:8.4px;font-weight:700;line-height:10.6px;color:var(--text);width:170px}
.step svg{flex:none;margin-top:2px}
.footer-name{position:absolute;left:40px;top:722px;font-size:11px;font-weight:700;color:var(--blue-dark)}
.footer-contact{position:absolute;left:40px;top:739px;display:flex;gap:16px;font-size:11px;font-weight:700;color:var(--blue-dark)}
.footer-contact span{display:flex;align-items:center;gap:5px}
</style>
</head>
<body>
<svg width="0" height="0" style="position:absolute">
  <symbol id="tick" viewBox="0 0 12 12"><circle cx="6" cy="6" r="6"/><path d="M3.3 6.2l1.8 1.8 3.6-3.8" fill="none" stroke="#fff" stroke-width="1.6" stroke-linecap="round" stroke-linejoin="round"/></symbol>
</svg>

<section class="page page--front">
  <svg class="layer" viewBox="0 0 544 769">
    <path d="M0 0H544V300H310V376C295 382 270 388 230 392C140 398 60 372 0 352Z" fill="#3d5675"/>
    <path d="M0 352C60 372 140 398 230 392C270 388 295 382 310 376V392C240 412 150 424 80 414C50 410 20 404 0 398Z" fill="#f4c955"/>
  </svg>
  <div class="photo front-photo" role="img" aria-label="Zwei Techniker mit Laptop auf einem Dach mit Solarmodulen"></div>
  <div class="brand front-brand"><span class="brand__dot"></span>SONNWERK SERVICE GMBH</div>
  <h1 class="headline front-title">Photovoltaikanlagen Neubau</h1>
  <h2 class="headline front-sub">Solaranlagen vom Niederrhein</h2>
  <p class="front-intro">Wir von der Sonnwerk Service GmbH sind Marktführer, wenn es um die Rundum-Betreuung im Bereich von Photovoltaikanlagen, Photovoltaik Wartung und die Installation von Solaranlagen geht. Mit Sitz am Niederrhein in Xanten sind wir Ansprechpartner Nummer 1 in ganz NRW für die neueste Solaranlagen-Technik.</p>
  <div class="photo module-photo" role="img" aria-label="Produktfoto eines schwarzen Solarmoduls"></div>
  <h2 class="headline spec-title">Solarmodule</h2>
  <table class="spec">
    <tr><td>Hersteller</td><td>KE-Lumin</td></tr>
    <tr><td>Type</td><td>KLM54-435/FB</td></tr>
    <tr><td>Leistung</td><td>435 Wp</td></tr>
    <tr><td>Wirkungsgrad</td><td>21,8 %</td></tr>
    <tr><td>Herstellergarantie</td><td>25 Jahre</td></tr>
    <tr><td>Leistungsgarantie</td><td>30 Jahre / 87.40%</td></tr>
    <tr><td>Zelltyp</td><td>monokristalline Halbzellen</td></tr>
  </table>
  <svg class="layer" viewBox="0 0 544 769">
    <path d="M0 697C60 674 130 664 200 666C300 670 380 712 460 712C500 712 525 690 544 662V769H0Z" fill="#3d5675"/>
    <path d="M0 722C60 708 150 702 250 706C370 712 460 726 544 708V769H0Z" fill="#f4c955"/>
  </svg>
  <p class="cta">BERATUNG<br>GEWÜNSCHT?</p>
  <p class="cta-phone"><span>Rufen Sie uns an:</span>
    <svg width="15" height="15" viewBox="0 0 24 24"><path fill="#33496a" d="M6.6 10.8a15.1 15.1 0 0 0 6.6 6.6l2.2-2.2c.3-.3.7-.4 1-.2 1.1.4 2.3.6 3.6.6.6 0 1 .4 1 1V20c0 .6-.4 1-1 1A17 17 0 0 1 3 4c0-.6.4-1 1-1h3.5c.6 0 1 .4 1 1 0 1.3.2 2.5.6 3.6.1.3 0 .7-.2 1z"/></svg>02832 4410270</p>
</section>

<section class="page page--back">
  <div class="photo back-photo" role="img" aria-label="Solarmodule auf einem Dach im Abendlicht"></div>
  <svg class="layer" viewBox="0 0 544 769">
    <path d="M0 250H544V320C500 292 440 286 380 300C260 336 120 356 0 336Z" fill="#f4c955"/>
    <path d="M300 322C400 286 480 280 544 330V372C480 322 420 306 300 328Z" fill="#3d5675"/>
  </svg>
  <div class="brand back-brand"><span class="brand__dot"></span>SONNWERK SERVICE GMBH</div>
  <ul class="services">
    <li><svg width="10" height="10" fill="#33496a"><use href="#tick"/></svg>Transparentes Angebot</li>
    <li><svg width="10" height="10" fill="#33496a"><use href="#tick"/></svg>Netzanfrage</li>
    <li><svg width="10" height="10" fill="#33496a"><use href="#tick"/></svg>Markstammdatenregisterung<br>(Vergütung für verkaufen Strom)</li>
    <li><svg width="10" height="10" fill="#33496a"><use href="#tick"/></svg>Planung &amp; Auslegung<br>(internes Ingeneurbüro)</li>
    <li><svg width="10" height="10" fill="#33496a"><use href="#tick"/></svg>Montage Dach<br>(Dachdeckermeisterbetrieb)</li>
    <li><svg width="10" height="10" fill="#33496a"><use href="#tick"/></svg>Monate Elektro inkl. Zähersetzung<br>(Elektromeisterbetrieb)</li>
    <li><svg width="10" height="10" fill="#33496a"><use href="#tick"/></svg>Einweisung ins Monitoring (App)</li>
    <li><svg width="10" height="10" fill="#33496a"><use href="#tick"/></svg>After Sales Service</li>
    <li><svg width="10" height="10" fill="#33496a"><use href="#tick"/></svg>Service &amp; Wartung</li>
    <li><svg width="10" height="10" fill="#33496a"><use href="#tick"/></svg>Reinigung</li>
  </ul>
  <h1 class="headline claim">Bedarfgerechte<br>Beratung inkl.<br>Besichtung der<br><em>Immobilie</em></h1>
  <h2 class="headline why">Warum Sie sich jetzt eine Solaranlage zulegen sollten</h2>
  <div class="col-left">
    <h3>Photovoltaik-Förderung 2024:<br>Das müssen Hausbesitzer jetzt wissen...</h3>
    <p>Mit dem Beschluss der Schuldenbremse werden 2024 zahlreiche Förderprogramme gestrichen. Vor allem Ausgaben aus dem Klima- und Transformationsfonds werden geringer ausfallen. Dazu gehört auch die aktuelle Solarförderung, die laut Berger gekürzt werden könnte. Experten raten: Die Anschaffung lohnt sich jetzt, solange Sie von der „steuerfreien“ Anlage profitieren können.</p>
    <p>Bundesweite Förderung: Günstiger denn je Für Hausbesitzer ist es gerade so attraktiv wie noch nie, in eine eigene Solaranlage zu investieren. In Deutschland wurden seit Januar 2023 einige Förderprogramme und Steuererleichterungen für private Solaranlagen festgelegt. Die Höhe und Bedingungen der Förderung ist von verschiedenen Faktoren abhängig. Dazu gehören Größe der Solaranlage, Stromverbrauch und Anbieter. Durch Steuererleichterungen müssen Hausbesitzer momentan für eine Photovoltaikanlage keine Mehrwertsteuer, Einkommensteuer und Gewerbesteuer zahlen.</p>
    <p>Die Investition lohnt sich jetzt mehr denn je.</p>
  </div>
  <div class="divider"></div>
  <div class="col-right">
    <h3>In vier Schritten zur <u>eigenen</u><br>Solaranlage</h3>
    <div class="step"><svg width="10" height="10" fill="#f4c955"><use href="#tick"/></svg><div><h4>Beratung</h4><p>Wir beraten Sie umfassend über geeignete Solaranlagen-Produkte. Vereinbaren Sie am besten gleich Ihren vor-Ort-Termin</p></div></div>
    <div class="step"><svg width="10" height="10" fill="#f4c955"><use href="#tick"/></svg><div><h4>Fördermöglichkeiten</h4><p>Sie müssen sich nicht selbst um geeignete Fördermöglichkeiten kümmern. Dazu erhalten Sie eine detaillierte Beratung.</p></div></div>
    <div class="step"><svg width="10" height="10" fill="#f4c955"><use href="#tick"/></svg><div><h4>Planung &amp; Installation</h4><p>Sie müssen sich nicht selbst um geeignete Fördermöglichkeiten kümmern. Dazu erhalten Sie eine detaillierte Beratung.</p></div></div>
    <div class="step"><svg width="10" height="10" fill="#f4c955"><use href="#tick"/></svg><div><h4>Inbetriebnahme &amp; Monitoring</h4><p>Genießen Sie den Ertrag Ihrer neuen Solaranlage. Wir übernehmen die Fernwartung nach Inbetriebnahme.</p></div></div>
  </div>
  <svg class="layer" viewBox="0 0 544 769">
    <path d="M0 722C60 682 130 664 200 667C280 672 340 707 400 707C470 707 520 686 544 662V769H0Z" fill="#3d5675"/>
    <path d="M0 734C60 714 150 706 250 710C370 716 460 728 544 704V769H0Z" fill="#f4c955"/>
  </svg>
  <p class="footer-name">SONNWERK SERVICE GMBH</p>
  <div class="footer-contact">
    <span><svg width="10" height="10" viewBox="0 0 24 24"><path fill="#33496a" d="M12 2a7 7 0 0 0-7 7c0 5 7 13 7 13s7-8 7-13a7 7 0 0 0-7-7zm0 9.5a2.5 2.5 0 1 1 0-5 2.5 2.5 0 0 1 0 5z"/></svg>Lindenweg 8 · 46509 Xanten</span>
    <span><svg width="10" height="10" viewBox="0 0 24 24"><path fill="#33496a" d="M6.6 10.8a15.1 15.1 0 0 0 6.6 6.6l2.2-2.2c.3-.3.7-.4 1-.2 1.1.4 2.3.6 3.6.6.6 0 1 .4 1 1V20c0 .6-.4 1-1 1A17 17 0 0 1 3 4c0-.6.4-1 1-1h3.5c.6 0 1 .4 1 1 0 1.3.2 2.5.6 3.6.1.3 0 .7-.2 1z"/></svg>0 28 01 / 55 12 40</span>
    <span><svg width="10" height="10" viewBox="0 0 24 24"><circle cx="12" cy="12" r="9" fill="none" stroke="#33496a" stroke-width="2"/><path d="M3 12h18M12 3c3 3 3 15 0 18M12 3c-3 3-3 15 0 18" fill="none" stroke="#33496a" stroke-width="1.6"/></svg>sonnwerk-service.de</span>
  </div>
</section>
</body>
</html>
```